We need a card design for our company Harbor Lantern Partners. Our goal is to save people money on their disposal services. For this post card please put our logo in it. Please use these colors Pantone 576c and 418c or green and grey. We are giving you as the designer the opportunity to be creative with any other images. We are looking to have a fun eye catching postcard.
Please write:
Think you are stuck with your trash bill? Think again
We cut your neighbors disposal cost by 40%.

Please put down our information also,
Contact us
800.514.7262
melinda@plumcrest782.com
plumcrest782.com

```html
<!DOCTYPE html>
<html lang="en">
<head>
<meta charset="utf-8">
<title>Harbor Lantern Partners – Postcard</title>
<link rel="stylesheet" href="https://fonts.googleapis.com/css2?family=Roboto+Condensed:wght@400;700&display=swap">
<style>
  :root {
    --green: #6f9f52;
    --green-deep: #4f8a3a;
    --green-bright: #7fb23a;
    --green-pale: #e4efd9;
    --grey: #5a5b5d;
    --grey-light: #8a8b8d;
    --white: #ffffff;
    --stage: #ebe8e3;
    --line: #9a9a9a;
  }
  * { box-sizing: border-box; margin: 0; padding: 0; }
  html, body {
    width: 1200px; height: 500px; overflow: hidden;
    background: var(--stage);
    font-family: "Roboto Condensed", "Arial Narrow", sans-serif;
  }
  .card {
    position: absolute; top: 85px;
    width: 506px; height: 335px;
    background: var(--white);
    box-shadow: 0 2px 8px rgba(0,0,0,.25);
    overflow: hidden;
  }
  .card--front { left: 61px; }
  .card--back { left: 632px; }

  .front-wave { position: absolute; inset: 0; }
  .headline {
    position: absolute; left: 22px; top: 10px;
    color: var(--white); font-weight: 700; font-size: 25px;
  }
  .offer {
    position: absolute; left: 22px; top: 50px;
    color: var(--white); font-weight: 700; font-size: 21px; line-height: 1.32;
  }
  .brand {
    position: absolute; display: flex; align-items: center; gap: 8px;
    color: var(--grey); font-weight: 700;
  }
  .brand__mark { width: 22px; height: 22px; background: var(--grey); }
  .card--front .brand { left: 250px; top: 122px; font-size: 20px; }
  .photo-slot {
    position: absolute; left: 0; top: 140px; width: 238px; height: 195px;
    background: linear-gradient(160deg, #b9d98a 0%, #8fbf5c 45%, #5d7fa5 100%);
  }
  .mascot-slot {
    position: absolute; left: 248px; top: 208px; width: 46px; height: 68px;
    border-radius: 6px;
    background: linear-gradient(180deg, #a7d452, var(--green-bright));
  }
  .mission {
    position: absolute; right: 22px; top: 188px; text-align: right;
    color: var(--grey); font-weight: 700; font-size: 18px; line-height: 1.22;
  }
  .contact {
    position: absolute; right: 22px; top: 280px; text-align: right;
    color: var(--grey); font-size: 17px;
  }
  .contact__phone { color: var(--green); font-weight: 700; font-size: 22px; margin-left: 4px; }
  .contact__email { font-size: 12.5px; margin-top: 4px; }
  .contact__email span { color: var(--green); }

  .back-fade {
    position: absolute; left: 0; right: 0; bottom: 0; height: 190px;
    background: linear-gradient(180deg, var(--white) 0%, var(--green-pale) 100%);
  }
  .card--back .brand { left: 22px; top: 38px; font-size: 22px; }
  .web {
    position: absolute; left: 46px; top: 102px;
    color: var(--green); font-weight: 700; font-size: 15px; letter-spacing: 2px;
  }
  .stamp {
    position: absolute; left: 366px; top: 27px; width: 88px; height: 97px;
    border: 1.5px solid var(--grey); background: var(--white);
  }
  .symbol-slot {
    position: absolute; left: 20px; top: 198px; width: 114px; height: 118px;
    border-radius: 50%;
    background: radial-gradient(circle, #7fc36a 0%, #3f9a45 100%);
    opacity: .85;
  }
  .address-lines { position: absolute; left: 170px; top: 200px; width: 286px; }
  .address-lines span {
    display: block; height: 33px; border-bottom: 1px solid var(--line);
  }
  .address-lines span:first-child { height: 1px; }
</style>
</head>
<body>

<section class="card card--front">
  <svg class="front-wave" width="506" height="335" viewBox="0 0 506 335" aria-hidden="true">
    <path d="M0 0H506V92C430 96 330 132 240 168C150 200 70 210 0 214Z" fill="var(--green)"/>
    <path d="M506 104C420 108 320 142 236 176C160 206 80 218 0 222" fill="none" stroke="var(--green)" stroke-width="3" opacity=".55"/>
  </svg>
  <h1 class="headline">Think you are stuck with your trash bill?</h1>
  <p class="offer">We cut your neighbors<br>disposal cost by<br>40%</p>
  <div class="photo-slot" role="img" aria-label="Photo of a smiling woman holding a green recycling bag filled with plastic bottles"></div>
  <div class="brand"><span class="brand__mark"></span>Harbor Lantern Partners</div>
  <div class="mascot-slot" role="img" aria-label="Illustration of a cheerful green recycling bin character giving a thumbs up"></div>
  <p class="mission">Our goal is to save<br>people money on their<br>disposal services</p>
  <div class="contact">
    <p>Contact us:<span class="contact__phone">800.514.7262</span></p>
    <p class="contact__email">Email: <span>melinda@plumcrest782.com</span></p>
  </div>
</section>

<section class="card card--back">
  <div class="back-fade"></div>
  <div class="brand"><span class="brand__mark"></span>Harbor Lantern Partners</div>
  <p class="web">www.plumcrest782.com</p>
  <div class="stamp"></div>
  <div class="symbol-slot" role="img" aria-label="Large green recycling symbol illustration"></div>
  <div class="address-lines"><span></span><span></span><span></span><span></span></div>
</section>

</body>
</html>
```